Sports Nutrition line needs new label look/feel

We need a new label design for "Telmo",our Sports Nutrition line of vitamins, nutraceuticals, protein powders, and performance endurance products. We would like to see two separate designs, one blue and one red, as these are the two colors we are torn between. The labels should have the look/feel of a sports or fitness label, bold coloring, lettering, and even some use of holographic foiling.
Brands we would be similar to those found on pulsevaultshop.com and stridecraftnow.com. Brands we like in particular are QRT and Velmot.

Target Market(s)

Fitness enthusiasts,athletes, health nuts..

Industry/Entity Type

Nutrition

Font styles to use
Sans Serif
Decorative
Script

Colors
ec1f27
0692cd
0355a3
3276b5
f04a50

Requirements
Must have
• -Fitness look/feel
• -bold colors (preferably red and blue)
• -use of icons (eye health, brain, health, etc.)
• -"Fit" in "TelMO" must stand out
• -use tagline "Building Healthy Bodies"
Nice to have
• -holographic foiling elements
• -try to incorporate a molecular element (like those shown in the example labels)
Should not have
• -Light, calming colors
• -difficult to read fonts

```html
<!DOCTYPE html>
<html lang="en">
<head>
<meta charset="utf-8">
<title>TelMO Grape Seed Extract – Label Variants</title>
<link rel="stylesheet" href="https://fonts.googleapis.com/css2?family=Archivo+Black&family=Oswald:wght@500;600&family=Russo+One&display=swap">
<style>
  :root{
    --stage:#8b8b8e;
    --stage-dark:#6f6f72;
    --ink:#111111;
    --paper:#ffffff;
    --steel:#c9c9cc;
    --steel-text:#4a4a4d;
    --blue:#1f86d3;
    --blue-deep:#0355a3;
    --red:#ec1f27;
    --red-deep:#c3121a;
    --cap-dark:#1a1a1b;
    --cap-mid:#3a3a3c;
  }
  *{box-sizing:border-box;margin:0;padding:0}
  html,body{width:1200px;height:1200px;overflow:hidden}
  body{
    background:linear-gradient(180deg,var(--stage) 0%,var(--stage-dark) 100%);
    display:flex;align-items:center;justify-content:center;gap:40px;
  }
  .label{
    position:relative;width:540px;height:840px;background:var(--paper);
    overflow:hidden;box-shadow:0 12px 30px rgba(0,0,0,.35);
  }
  .label__top{position:absolute;left:0;top:0;width:540px;height:260px}
  .label__tagline{
    position:absolute;right:34px;top:150px;
    font-family:"Russo One",sans-serif;font-size:30px;line-height:1.15;color:#2a2a2a;
  }
  .label__molecule{position:absolute;right:22px;top:275px;width:120px;height:100px}
  .label__brand{
    position:absolute;left:30px;top:385px;
    font-family:"Archivo Black",sans-serif;font-size:118px;line-height:1;
    color:var(--ink);letter-spacing:-2px;white-space:nowrap;
  }
  .label__product{
    position:absolute;left:0;top:522px;width:540px;height:80px;
    background:linear-gradient(180deg,#f2f2f3 0%,var(--steel) 55%,#e6e6e8 100%);
    font-family:"Oswald",sans-serif;font-weight:600;font-size:56px;line-height:80px;
    text-align:center;color:var(--steel-text);letter-spacing:-1px;white-space:nowrap;
  }
  .label__panel{
    position:absolute;left:0;top:602px;width:540px;height:238px;
    display:flex;flex-direction:column;padding:14px 24px 20px;
  }
  .label--blue .label__panel{background:linear-gradient(180deg,var(--blue) 0%,var(--blue-deep) 100%)}
  .label--red .label__panel{background:linear-gradient(180deg,var(--red) 0%,var(--red-deep) 100%)}
  .label__claim{
    text-align:center;color:var(--paper);white-space:nowrap;
    font-family:"Oswald",sans-serif;font-weight:600;font-size:27px;line-height:36px;letter-spacing:-.5px;
  }
  .label__icons{display:flex;justify-content:space-between;align-items:center;padding:14px 10px 0}
  .label__icons svg{width:60px;height:60px;flex:none}
  .label__footer{
    margin-top:auto;
    display:flex;align-items:flex-end;justify-content:space-between;
  }
  .badge-free{font-family:"Oswald",sans-serif;font-weight:600;color:var(--ink);line-height:1}
  .badge-free__top{font-size:16px}
  .badge-free__mid{font-size:9px}
  .badge-free__bottom{font-size:18px}
  .zero-crash{font-family:"Russo One",sans-serif;color:var(--paper);text-align:right;line-height:.95}
  .zero-crash__big{font-size:34px}
  .zero-crash__small{font-size:16px;letter-spacing:1px;color:#e8e8e8}
  .servings{text-align:center;font-family:"Russo One",sans-serif;color:var(--paper)}
  .servings__count{font-size:24px;letter-spacing:1px}
  .servings__type{
    margin-top:6px;border:2px solid var(--ink);border-radius:6px;padding:2px 8px;
    font-size:12px;color:var(--ink);letter-spacing:1px;white-space:nowrap;
  }
</style>
</head>
<body>

  <section class="label label--blue">
    <svg class="label__top" viewBox="0 0 540 260" role="img" aria-label="Dark hexagon texture band">
      <defs>
        <linearGradient id="capBlue" x1="0" y1="0" x2="0" y2="1">
          <stop offset="0" stop-color="#3a3a3c"/><stop offset="1" stop-color="#1a1a1b"/>
        </linearGradient>
      </defs>
      <path d="M0 0H540V90C420 110 300 150 210 200C140 238 70 255 0 260Z" fill="url(#capBlue)"/>
    </svg>
    <div class="label__tagline">Building<br>Healthy<br>Bodies</div>
    <svg class="label__molecule" viewBox="0 0 130 110" aria-hidden="true">
      <line x1="25" y1="52" x2="85" y2="30" stroke="#3a7fc0" stroke-width="5"/>
      <line x1="85" y1="30" x2="112" y2="88" stroke="#9ab" stroke-width="5"/>
      <circle cx="25" cy="52" r="18" fill="#63b9ea"/>
      <circle cx="85" cy="30" r="24" fill="#1e7fd0"/>
      <circle cx="112" cy="88" r="17" fill="#c8ccd2"/>
    </svg>
    <div class="label__brand">TelMO</div>
    <div class="label__product">GRAPE SEED EXTRACT</div>
    <div class="label__panel">
      <p class="label__claim">ANTIOXIDANT FORMULA TO BOOST IMMUNITY</p>
      <div class="label__icons">
        <svg viewBox="0 0 70 70" aria-label="Joint"><rect x="24" y="4" width="22" height="26" rx="10" fill="#bfc3c8"/><rect x="24" y="40" width="22" height="26" rx="10" fill="#bfc3c8"/><circle cx="35" cy="35" r="7" fill="#fff"/></svg>
        <svg viewBox="0 0 70 70" aria-label="Target"><circle cx="35" cy="35" r="20" fill="none" stroke="#fff" stroke-width="7"/><circle cx="35" cy="35" r="6" fill="#fff"/><path d="M35 2V18M35 52V68M2 35H18M52 35H68" stroke="#fff" stroke-width="6"/></svg>
        <svg viewBox="0 0 70 70" aria-label="Strength"><path d="M18 8C30 4 38 8 36 18L30 22C30 34 34 40 44 36C56 30 64 40 60 52C56 64 30 66 16 60C8 56 8 40 12 28C14 18 12 12 18 8Z" fill="#fff"/></svg>
        <svg viewBox="0 0 70 70" aria-label="Cells" fill="#fff"><polygon points="20,8 30,13 30,24 20,29 10,24 10,13"/><polygon points="40,8 50,13 50,24 40,29 30,24 30,13"/><polygon points="30,26 40,31 40,42 30,47 20,42 20,31"/><polygon points="50,26 60,31 60,42 50,47 40,42 40,31"/><polygon points="40,44 50,49 50,60 40,65 30,60 30,49"/></svg>
        <svg viewBox="0 0 70 70" aria-label="Energy"><polygon points="42,2 16,40 32,40 24,68 54,26 38,26" fill="#ec1f27"/></svg>
      </div>
      <div class="label__footer">
        <div class="badge-free"><div class="badge-free__top">BANNED</div><div class="badge-free__mid">SUBSTANCE</div><div class="badge-free__bottom">FREE ✓</div></div>
        <div class="zero-crash"><div class="zero-crash__big">ZERO</div><div class="zero-crash__small">CRASH</div></div>
        <div class="servings"><div class="servings__count">90 SERVINGS</div><div class="servings__type">DIETARY SUPPLEMENT</div></div>
      </div>
    </div>
  </section>

  <section class="label label--red">
    <svg class="label__top" viewBox="0 0 540 260" role="img" aria-label="Dark hexagon texture band">
      <defs>
        <linearGradient id="capRed" x1="0" y1="0" x2="0" y2="1">
          <stop offset="0" stop-color="#3a3a3c"/><stop offset="1" stop-color="#1a1a1b"/>
        </linearGradient>
      </defs>
      <path d="M0 0H540V90C420 110 300 150 210 200C140 238 70 255 0 260Z" fill="url(#capRed)"/>
    </svg>
    <div class="label__tagline">Building<br>Healthy<br>Bodies</div>
    <svg class="label__molecule" viewBox="0 0 130 110" aria-hidden="true">
      <line x1="25" y1="52" x2="85" y2="30" stroke="#d84a30" stroke-width="5"/>
      <line x1="85" y1="30" x2="112" y2="88" stroke="#9ab" stroke-width="5"/>
      <circle cx="25" cy="52" r="18" fill="#f26a4a"/>
      <circle cx="85" cy="30" r="24" fill="#e8302a"/>
      <circle cx="112" cy="88" r="17" fill="#c8ccd2"/>
    </svg>
    <div class="label__brand">TelMO</div>
    <div class="label__product">GRAPE SEED EXTRACT</div>
    <div class="label__panel">
      <p class="label__claim">ANTIOXIDANT FORMULA TO BOOST IMMUNITY</p>
      <div class="label__icons">
        <svg viewBox="0 0 70 70" aria-label="Joint"><rect x="24" y="4" width="22" height="26" rx="10" fill="#bfc3c8"/><rect x="24" y="40" width="22" height="26" rx="10" fill="#bfc3c8"/><circle cx="35" cy="35" r="7" fill="#fff"/></svg>
        <svg viewBox="0 0 70 70" aria-label="Target"><circle cx="35" cy="35" r="20" fill="none" stroke="#fff" stroke-width="7"/><circle cx="35" cy="35" r="6" fill="#fff"/><path d="M35 2V18M35 52V68M2 35H18M52 35H68" stroke="#fff" stroke-width="6"/></svg>
        <svg viewBox="0 0 70 70" aria-label="Strength"><path d="M18 8C30 4 38 8 36 18L30 22C30 34 34 40 44 36C56 30 64 40 60 52C56 64 30 66 16 60C8 56 8 40 12 28C14 18 12 12 18 8Z" fill="#fff"/></svg>
        <svg viewBox="0 0 70 70" aria-label="Cells" fill="#fff"><polygon points="20,8 30,13 30,24 20,29 10,24 10,13"/><polygon points="40,8 50,13 50,24 40,29 30,24 30,13"/><polygon points="30,26 40,31 40,42 30,47 20,42 20,31"/><polygon points="50,26 60,31 60,42 50,47 40,42 40,31"/><polygon points="40,44 50,49 50,60 40,65 30,60 30,49"/></svg>
        <svg viewBox="0 0 70 70" aria-label="Energy"><polygon points="42,2 16,40 32,40 24,68 54,26 38,26" fill="#b9bcc1"/></svg>
      </div>
      <div class="label__footer">
        <div class="badge-free"><div class="badge-free__top">BANNED</div><div class="badge-free__mid">SUBSTANCE</div><div class="badge-free__bottom">FREE ✓</div></div>
        <div class="zero-crash"><div class="zero-crash__big">ZERO</div><div class="zero-crash__small">CRASH</div></div>
        <div class="servings"><div class="servings__count">90 SERVINGS</div><div class="servings__type">DIETARY SUPPLEMENT</div></div>
      </div>
    </div>
  </section>

</body>
</html>
```